ZELKO Ice Cream Logo & Packaging Project

We need a logo and ice cream packaging for our new company Zelko.

The company is based in Freetown, Sierra Leone, West Africa. It will be a large scale business, going national. For example the minimum order is 120.000 pieces of the small cup. Zelko will produce and sell affordable frozen dairy products directly to consumers through a unique street vending system.

Your design will have great exposure.

The word ZELKO refers to anything or something which is WONDERFUL OR EXTRAORDINARY. ZELKO is something EXPLOSIVE. Also ZELKO refers to a shape, The ZELKO shape is round,just like an ICE CREAM BALL.

We thought the design could incorporate and exploding rays around an ice cream ball or cone. The market responds well to colours and visuals.

People may use the word ZELKO in this context :

1-A man who has a very nice STRONG and TONED,and full of MUSCLES body is a ZELKO
2 -A great EVENT,big HUGE CONCERT is a ZELKO
3 -A powerful and tasty ICE CREAM is a ZELKO.

There are several packagings to design. See attached documents for sizes, but the first task is the logo and the small cup.

The lid will be transparent plastic so you can see the ice cream, so we don't need the flavours on the label.

100-120ml tub Small cup sleeve and full lid

Required info includes :

Tavrin Ice Cream Co, Wellington, Freetown, Sierra Leone.

Ingredients : sugar, glucose solids, milk, bean gum, natural flavour, colour, milk chocolate

Afterwards we will need packaging for :

1050ml oval tub sleeve and full lid

2120ml oval tub sleeve and lid full

standard ice cream cone sleeve.

standard ice lolly sleeve (note sleeve will be transparent)

trolley cart image 60cm wide x 60cm heigh approx

All ages and nationalities. The company is based in Freetown, Sierra Leone, West Africa which is a 3rd world country. The market respond well to colours and visuals.

It Company

Serif
Sans Serif

• Tavrin Ice Cream Co, Wellington, Freetown, Sierra Leone.
• Ingredients : sugar, glucose solids, milk, bean gum, natural flavour, colour, milk chocolate.
• The word ZELKO refers to anything or something which is WONDERFUL OR EXTRAORDINARY. ZELKO is something EXPLOSIVE. Also ZELKO refers to a shape, The ZELKO shape is round,just like an ICE CREAM BALL.
• We thought the design could incorporate and exploding rays around an ice cream ball or cone.

```html
<!DOCTYPE html>
<html lang="en">
<head>
<meta charset="utf-8">
<title>Zelko Ice Cream – Cup Sleeves and Lids</title>
<link rel="stylesheet" href="https://fonts.googleapis.com/css2?family=Lilita+One&family=Roboto:wght@500&display=swap">
<style>
  :root {
    --canvas: #ffffff;
    --stage: #f1f1f1;
    --magenta: #e0147f;
    --orange: #ee5a24;
    --sky: #5aa9e6;
    --yellow: #fbe715;
    --cocoa: #3b2418;
    --maroon: #6b1f2a;
    --white: #ffffff;
    --edge: #dcdcdc;
  }
  * { margin: 0; padding: 0; box-sizing: border-box; }
  html, body { width: 1200px; height: 1000px; overflow: hidden; background: var(--canvas); }
  .canvas { position: relative; width: 1200px; height: 1000px; }

  .product-row {
    position: absolute; left: 168px; width: 578px; height: 375px;
    background: var(--stage);
  }
  .row-chocolate { top: 132px; }
  .row-banana { top: 510px; }

  .sleeve {
    position: absolute; left: 22px; top: 40px; width: 290px; height: 305px;
    clip-path: polygon(0 0, 100% 0, 94% 100%, 6% 100%);
    overflow: hidden;
  }
  .sleeve-chocolate { background: var(--white); }
  .sleeve-banana { background: var(--yellow); }

  .lid {
    position: absolute; left: 340px; top: 72px; width: 236px; height: 236px;
    border-radius: 50%; overflow: hidden;
    box-shadow: 0 0 0 1px var(--edge);
  }
  .lid-chocolate { background: var(--white); }
  .lid-banana { background: var(--yellow); }

  .burst { position: absolute; }
  .burst svg { display: block; width: 100%; height: 100%; }

  .wordmark {
    position: absolute; left: 0; right: 0; text-align: center;
    font-family: "Lilita One", sans-serif; font-weight: 400;
    letter-spacing: 2px; line-height: 1; white-space: nowrap;
  }
  .wordmark-magenta { color: var(--magenta); }
  .wordmark-orange { color: var(--orange); }
  .wordmark-white { color: var(--white); }

  .flavour-tag {
    position: absolute; left: 50%; transform: translateX(-50%);
    font-family: "Roboto", sans-serif; font-weight: 500;
    white-space: nowrap; padding: 2px 7px; letter-spacing: 0.3px;
  }
  .flavour-dark { background: var(--cocoa); color: var(--white); }
  .flavour-light { background: var(--white); color: var(--maroon); }

  .logo-variant { position: absolute; }
  .logo-classic { left: 760px; top: 140px; width: 300px; height: 240px; }
  .logo-star { left: 765px; top: 385px; width: 272px; height: 260px; }
  .logo-cool { left: 768px; top: 650px; width: 266px; height: 235px; }
</style>
</head>
<body>
<main class="canvas">
  <svg width="0" height="0" style="position:absolute" aria-hidden="true">
    <defs>
      <radialGradient id="glowWarm" cx="50%" cy="50%" r="50%">
        <stop offset="0" stop-color="#fde21a"/>
        <stop offset="0.45" stop-color="#fbc61a"/>
        <stop offset="0.72" stop-color="#f26a21"/>
        <stop offset="0.86" stop-color="#e8262b" stop-opacity="0.85"/>
        <stop offset="1" stop-color="#e8262b" stop-opacity="0"/>
      </radialGradient>
      <radialGradient id="glowBright" cx="50%" cy="50%" r="50%">
        <stop offset="0" stop-color="#ffffff"/>
        <stop offset="0.6" stop-color="#ffffff"/>
        <stop offset="0.82" stop-color="#fde21a"/>
        <stop offset="0.93" stop-color="#8a2a2e" stop-opacity="0.7"/>
        <stop offset="1" stop-color="#8a2a2e" stop-opacity="0"/>
      </radialGradient>
      <radialGradient id="glowCool" cx="50%" cy="50%" r="50%">
        <stop offset="0" stop-color="#9fe3ec"/>
        <stop offset="0.4" stop-color="#39b6c8"/>
        <stop offset="0.75" stop-color="#5b3aa0"/>
        <stop offset="1" stop-color="#5b3aa0" stop-opacity="0"/>
      </radialGradient>
    </defs>
  </svg>

  <section class="product-row row-chocolate">
    <div class="sleeve sleeve-chocolate">
      <div class="burst" style="left:10px;top:10px;width:270px;height:270px">
        <svg viewBox="0 0 270 270" role="img" aria-label="Comic explosion burst in red and yellow with smoke puffs and orange halftone dots">
          <circle cx="135" cy="135" r="135" fill="url(#glowWarm)"/>
        </svg>
      </div>
      <p class="wordmark wordmark-magenta" style="top:106px;font-size:80px">ZELKO</p>
      <p class="flavour-tag flavour-dark" style="top:282px;font-size:11px">CHOCOLATE + VANNILA</p>
    </div>
    <div class="lid lid-chocolate">
      <div class="burst" style="left:18px;top:18px;width:200px;height:200px">
        <svg viewBox="0 0 200 200" role="img" aria-label="Comic explosion burst in red and yellow with smoke puffs">
          <circle cx="100" cy="100" r="100" fill="url(#glowWarm)"/>
        </svg>
      </div>
      <p class="wordmark wordmark-magenta" style="top:86px;font-size:44px">ZELKO</p>
      <p class="flavour-tag flavour-dark" style="top:138px;font-size:9px">CHOCOLATE + VANNILA</p>
    </div>
  </section>

  <section class="product-row row-banana">
    <div class="sleeve sleeve-banana">
      <div class="burst" style="left:5px;top:5px;width:280px;height:280px">
        <svg viewBox="0 0 280 280" role="img" aria-label="Comic starburst with white centre and yellow rays outlined in maroon">
          <circle cx="140" cy="140" r="140" fill="url(#glowBright)"/>
        </svg>
      </div>
      <p class="wordmark wordmark-orange" style="top:104px;font-size:84px">ZELKO</p>
      <p class="flavour-tag flavour-light" style="top:283px;font-size:11px">BANANA</p>
    </div>
    <div class="lid lid-banana">
      <div class="burst" style="left:20px;top:20px;width:196px;height:196px">
        <svg viewBox="0 0 196 196" role="img" aria-label="Comic starburst with white centre and maroon outline">
          <circle cx="98" cy="98" r="98" fill="url(#glowBright)"/>
        </svg>
      </div>
      <p class="wordmark wordmark-orange" style="top:92px;font-size:44px">ZELKO</p>
      <p class="flavour-tag flavour-light" style="top:176px;font-size:9px">BANANA</p>
    </div>
  </section>

  <section class="logo-variant logo-classic">
    <div class="burst" style="left:0;top:0;width:300px;height:240px">
      <svg viewBox="0 0 300 240" role="img" aria-label="Red and yellow comic explosion with smoke puffs around the wordmark">
        <ellipse cx="150" cy="120" rx="150" ry="120" fill="url(#glowWarm)"/>
      </svg>
    </div>
    <p class="wordmark wordmark-magenta" style="top:88px;font-size:60px">ZELKO</p>
  </section>

  <section class="logo-variant logo-star">
    <div class="burst" style="left:0;top:0;width:272px;height:260px">
      <svg viewBox="0 0 272 260" role="img" aria-label="Yellow and white comic starburst outlined in maroon around the wordmark">
        <ellipse cx="136" cy="130" rx="136" ry="130" fill="url(#glowBright)"/>
      </svg>
    </div>
    <p class="wordmark wordmark-orange" style="top:100px;font-size:60px">ZELKO</p>
  </section>

  <section class="logo-variant logo-cool">
    <div class="burst" style="left:0;top:0;width:266px;height:235px">
      <svg viewBox="0 0 266 235" role="img" aria-label="Violet and teal comic burst with pale blue bubbles and halftone dots around the wordmark">
        <ellipse cx="133" cy="118" rx="133" ry="117" fill="url(#glowCool)"/>
      </svg>
    </div>
    <p class="wordmark wordmark-white" style="top:90px;font-size:58px">ZELKO</p>
  </section>
</main>
</body>
</html>
```